Cause bitches need love too!

I am creating an ad campaign. It will be a series of featured dogs in our shelter and they will contain a picture of the dog wich should be big enough to see on a yard sign and will change every week. I am placing the signs so that they lead you to the shelter. This is why I am also including the copy that says "you're almost there".

I have 4 tag lines:

1. Find unconditional Love.
2. She'll Love you furever!
3. He'll always listen.
4. Meet your new BFF

You're almost there 318 W Harrowgate Ln
Open 10 - 7/Tues-Sat

The dimensions for the sign are 24" wide and 18" high

Every week we will have a different picture of a different dog (hopefully last week's dog gets adopted). Anyhow, I am printing out yard signs, meaning that instead of printing 160 different signs it would be ideal just to replace the photo. So far the copy that is permanent is: "You're almost there. 318 W. Harrowgate Ln."

I could silhouette the image of the dog as well and super impose it on the sign, that's also a consideration, but ideally if I could have 4 tag lines I could print 40 signs of each and just replace the photo manually each week from my printer that would save costs.
Updates

Not enough designs to chose from and I edited the brief and committed to pay no matter what to increase the amount of designs as per your suggestions.

Target Market(s)

Animal lovers

Industry/Entity Type

Campaign

Font styles to use
Sans Serif

Colors

Designer to choose colors to be used in the design.

Requirements
Must have
• The dimensions for the sign are 24" wide and 18" high
Nice to have
• I want the signs to be hip, they should have a positive feel to them. You can alter the photos if you like. I am even open to new copy if you think something else works better.

```html
<!DOCTYPE html>
<html lang="en">
<head>
<meta charset="utf-8">
<title>Find Unconditional Love – Shelter Yard Sign</title>
<link rel="stylesheet" href="https://fonts.googleapis.com/css2?family=Antonio:wght@700&family=Josefin+Sans:wght@600&family=Libre+Baskerville&display=swap">
<style>
  :root {
    --frame: #2b2a2b;
    --cream: #fcf5ec;
    --plum: #4a1530;
    --ink: #1c1c1c;
    --muted: #3d3a38;
    --photo-light: #b3aeaf;
    --photo-mid: #8d8686;
    --photo-dog: #7e6f66;
  }
  * { margin: 0; padding: 0; box-sizing: border-box; }
  html, body { width: 1200px; height: 900px; overflow: hidden; background: var(--frame); }
  .sign {
    position: relative;
    width: 1200px;
    height: 900px;
    background: var(--frame);
    overflow: hidden;
  }
  .dog-photo {
    position: absolute;
    left: 11px; top: 11px;
    width: 816px; height: 878px;
    background:
      radial-gradient(ellipse 55% 60% at 40% 55%, var(--photo-dog) 0%, rgba(126,111,102,0.6) 45%, rgba(126,111,102,0) 75%),
      linear-gradient(180deg, var(--photo-light) 0%, var(--photo-mid) 100%);
  }
  .info-panel {
    position: absolute;
    left: 827px; top: 11px;
    width: 362px; height: 878px;
    background: var(--cream);
  }
  .headline { font-size: inherit; font-weight: inherit; }
  .tagline {
    position: absolute;
    font-family: "Antonio", sans-serif;
    font-weight: 700;
    color: var(--plum);
    text-transform: uppercase;
    font-size: 101px;
    line-height: 1;
    letter-spacing: -1px;
    white-space: nowrap;
    transform-origin: left top;
    transform: scaleX(0.93);
  }
  .tagline-find { left: 606px; top: 321px; }
  .tagline-unconditional { left: 606px; top: 419px; }
  .tagline-love { left: 832px; top: 515px; }
  .accent-dash {
    position: absolute;
    left: 784px;
    width: 89px; height: 10px;
    border-radius: 5px;
    background: var(--plum);
  }
  .accent-dash-top { top: 371px; }
  .accent-dash-bottom { top: 651px; }
  .divider {
    position: absolute;
    left: 840px; top: 700px;
    width: 343px;
    border-top: 2px dashed var(--ink);
  }
  .directions {
    position: absolute;
    left: 849px; top: 726px;
    font-family: "Josefin Sans", sans-serif;
    font-weight: 600;
    font-size: 30px;
    color: var(--ink);
    white-space: nowrap;
  }
  .visit-details {
    position: absolute;
    right: 40px; top: 783px;
    text-align: right;
    font-family: "Libre Baskerville", serif;
    font-size: 17px;
    line-height: 27px;
    color: var(--muted);
    list-style: none;
  }
</style>
</head>
<body>
<main class="sign">
  <div class="dog-photo" role="img" aria-label="Portrait of the featured shelter dog, a grey and white pit bull mix, against a grey studio backdrop"></div>
  <section class="info-panel"></section>

  <h1 class="headline">
    <span class="tagline tagline-find">Find</span>
    <span class="tagline tagline-unconditional">Unconditional</span>
    <span class="tagline tagline-love">Love.</span>
  </h1>
  <span class="accent-dash accent-dash-top"></span>
  <span class="accent-dash accent-dash-bottom"></span>

  <div class="divider"></div>
  <p class="directions">You’re Almost There</p>
  <ul class="visit-details">
    <li>318 W Harrowgate Ln</li>
    <li>Open 10am - 7pm</li>
    <li>Tuesday - Saturday</li>
  </ul>
</main>
</body>
</html>
```